Business Consulting Company needs a business card designed

We need a business card in Brisbane Australia for a company called " Brindlewood Consulting Group". I would like to see the designs either in purple or green color

```html
<!DOCTYPE html>
<html lang="en">
<head>
<meta charset="utf-8">
<title>Brindlewood Consulting Group – Business Card</title>
<link rel="stylesheet" href="https://fonts.googleapis.com/css2?family=Open+Sans:wght@400;600;700&display=swap">
<style>
  :root {
    --purple: #962d88;
    --purple-deep: #8a2a7e;
    --card-white: #f1f1f1;
    --ink-grey: #6b6b6b;
    --backdrop: #e4e4e4;
    --text-light: #ffffff;
  }
  * { box-sizing: border-box; margin: 0; padding: 0; }
  html, body {
    width: 1200px;
    height: 1000px;
    overflow: hidden;
    background: var(--backdrop);
    font-family: "Open Sans", Arial, sans-serif;
  }
  .canvas {
    position: relative;
    width: 1200px;
    height: 1000px;
  }

  /* Card back (portrait) */
  .card-back {
    position: absolute;
    left: 90px;
    top: 190px;
    width: 360px;
    height: 620px;
    background: radial-gradient(circle at 50% 48%, #ffffff 0%, #f3e6f0 14%, #c98bbf 38%, var(--purple) 72%, var(--purple-deep) 100%);
    box-shadow: 0 6px 18px rgba(0,0,0,0.18);
  }
  .card-back .brand-mark {
    position: absolute;
    left: 0;
    right: 0;
    top: 270px;
    text-align: center;
    color: var(--purple);
    font-weight: 700;
    font-size: 30px;
    letter-spacing: 0.5px;
  }
  .card-back .brand-mark .dot {
    display: block;
    width: 26px;
    height: 26px;
    margin: 0 auto 12px;
    border-radius: 50%;
    background: var(--purple);
  }
  .card-back .website {
    position: absolute;
    right: 22px;
    top: 50%;
    transform: translate(50%, -50%) rotate(-90deg);
    transform-origin: center;
    white-space: nowrap;
    color: var(--purple);
    font-size: 15px;
    letter-spacing: 3px;
    font-weight: 600;
  }

  /* Card front (landscape) */
  .card-front {
    position: absolute;
    left: 500px;
    top: 320px;
    width: 620px;
    height: 360px;
    display: flex;
    box-shadow: 0 6px 18px rgba(0,0,0,0.18);
  }
  .card-front .identity {
    position: relative;
    width: 360px;
    background: var(--card-white);
    padding: 70px 30px 0 40px;
  }
  .identity .company {
    color: var(--purple);
    font-weight: 700;
    font-size: 30px;
    line-height: 1.15;
  }
  .identity .company .dot {
    display: inline-block;
    width: 22px;
    height: 22px;
    margin-bottom: 14px;
    background: var(--purple);
    border-radius: 50%;
  }
  .identity .website {
    position: absolute;
    left: 40px;
    bottom: 34px;
    color: var(--purple);
    font-size: 15px;
    font-weight: 600;
    letter-spacing: 3px;
  }
  .card-front .contact-panel {
    flex: 1;
    background: var(--purple);
    color: var(--text-light);
    padding: 26px 26px 26px 20px;
    text-align: right;
    display: flex;
    flex-direction: column;
  }
  .contact-panel .person-name {
    font-weight: 700;
    font-size: 17px;
  }
  .contact-panel .person-title {
    font-size: 11px;
    margin-top: 2px;
  }
  .contact-panel .address {
    margin-top: 34px;
    font-size: 12px;
    line-height: 1.5;
  }
  .contact-panel .lines {
    margin-top: auto;
    text-align: left;
    font-size: 12px;
    line-height: 1.5;
    padding-left: 16px;
  }
</style>
</head>
<body>
<main class="canvas">

  <section class="card-back" aria-label="Business card back">
    <div class="brand-mark"><span class="dot"></span>Brindlewood</div>
    <div class="website">www.brindlewoodcg.com.au</div>
  </section>

  <section class="card-front" aria-label="Business card front">
    <div class="identity">
      <div class="company"><span class="dot"></span><br>Brindlewood<br>Consulting Group</div>
      <div class="website">www.brindlewoodcg.com.au</div>
    </div>
    <div class="contact-panel">
      <div class="person-name">Your Name</div>
      <div class="person-title">Title</div>
      <div class="address">Address line 1<br>12, line two<br>Line three, Zip, AU</div>
      <div class="lines">
        T: + 61 (0) 00 0000 0000<br>
        M: + 61 (0) 0000 000 000<br>
        E: info@brindlewoodcg.com.au
      </div>
    </div>
  </section>

</main>
</body>
</html>
```